Classic Minimalistic Business Card

Design a classic, minimalistic Business Card. Please find inspiration in the attached Classic Minimalistic examples. My information:
Name: Glen Ovamir
Company: Ovamir Capital
Logo: OC
Address: 1470 N Thornwick Rd, Suite 210 | Ashvale, IL 60182
Phone: 630-555-0192
Email: glenovamir@pvt.insure
Slogan: Building Strength Through Capital

Feel free to leave out any of the information above except my name.

I have selected Double-sided, but I am also open to Single-sided

Target Market(s)

22-70. income greater than 150k/year

Industry/Entity Type

Finance

Contact Information for Business Card

See Project Description

Requirements
Must have
• Ivory or "antiqued" background similar to the reference pictures

```html
<!DOCTYPE html>
<html lang="en">
<head>
<meta charset="utf-8">
<title>Ovamir Capital — Business Card</title>
<link rel="stylesheet" href="https://fonts.googleapis.com/css2?family=Cormorant+Garamond:wght@400;500&display=swap">
<style>
  :root {
    --ivory: #efe4d1;
    --ink: #141210;
  }
  html, body {
    margin: 0;
    padding: 0;
    width: 1200px;
    height: 900px;
    overflow: hidden;
    background: var(--ivory);
  }
  .card {
    position: relative;
    width: 1200px;
    height: 900px;
    color: var(--ink);
    font-family: "Cormorant Garamond", Georgia, serif;
  }
  .brand-mark {
    position: absolute;
    left: 148px;
    top: 218px;
    width: 138px;
    height: 138px;
  }
  .brand-name,
  .tagline,
  .person-name,
  .contact-line {
    position: absolute;
    margin: 0;
    line-height: 1;
    white-space: nowrap;
    font-weight: 500;
  }
  .brand-name {
    left: 319px;
    top: 232px;
    font-size: 72px;
    letter-spacing: 0.5px;
  }
  .tagline {
    left: 321px;
    top: 306px;
    font-size: 31px;
  }
  .person-name {
    left: 149px;
    top: 503px;
    font-size: 50px;
  }
  .divider {
    position: absolute;
    left: 151px;
    top: 564px;
    width: 678px;
    height: 0;
    border-top: 1.5px solid var(--ink);
  }
  .contact-line {
    left: 149px;
    font-size: 32px;
  }
  .contact-address { top: 586px; }
  .contact-phone { top: 633px; }
  .contact-email { top: 680px; }
</style>
</head>
<body>
  <main class="card">
    <svg class="brand-mark" viewBox="0 0 138 138" aria-hidden="true">
      <circle cx="69" cy="69" r="67" fill="none" stroke="#141210" stroke-width="2"/>
    </svg>
    <p class="brand-name">Ovamir Capital</p>
    <p class="tagline">Building Strength Through Capital</p>

    <h1 class="person-name">Glen Ovamir</h1>
    <div class="divider"></div>
    <p class="contact-line contact-address">1470 N Thornwick Rd, Suite 210 | Ashvale, IL 60182</p>
    <p class="contact-line contact-phone">630-555-0192</p>
    <p class="contact-line contact-email">glenovamir@pvt.insure</p>
  </main>
</body>
</html>
```